July 4th Postcard to existing clients

5x7 postcard wishing our clients happy 4th of July. Card should read on the back "Thank You For Being A Valued Client!. Stay Safe And Enjoy Your Independence Day Celebrations!"

Patriotic theme with fireworks is ideal. We are a law firm so should still have a feel of professionalism while still being fun since it is for a fun holiday.

```html
<!DOCTYPE html>
<html lang="en">
<head>
<meta charset="utf-8">
<title>Independence Day Client Postcard</title>
<link href="https://fonts.googleapis.com/css2?family=Great+Vibes&family=Cinzel:wght@400;700&family=Montserrat:wght@500&family=Roboto+Slab:wght@300&display=swap" rel="stylesheet">
<style>
  :root {
    --navy-deep: #15123f;
    --navy: #1d2a6e;
    --sky: #4aa6e4;
    --sky-light: #8fd2f5;
    --balloon-red: #c8202e;
    --balloon-white: #e9ecf2;
    --white: #ffffff;
    --text-soft: #dcdff0;
    --grey-brand: #666666;
    --ink-blue: #2f3e72;
    --link-blue: #3f82c8;
    --stamp-line: #222222;
  }
  * { margin: 0; padding: 0; box-sizing: border-box; }
  html, body { width: 1200px; height: 856px; overflow: hidden; background: var(--white); }
  .postcard { position: relative; width: 1200px; height: 856px; background: var(--white); }

  .greeting-panel {
    position: absolute; left: 0; top: 0; width: 574px; height: 856px; overflow: hidden;
  }
  .celebration-art {
    position: absolute; inset: 0;
    background:
      linear-gradient(90deg, var(--balloon-red) 0 12%, var(--balloon-white) 12% 25%, var(--navy) 25% 37%, var(--balloon-red) 37% 50%, var(--balloon-white) 50% 62%, var(--navy) 62% 72%, var(--balloon-red) 72% 86%, var(--balloon-white) 86% 100%) top / 100% 130px no-repeat,
      radial-gradient(ellipse at 50% 55%, var(--sky-light) 0%, var(--sky) 30%, transparent 60%),
      linear-gradient(180deg, var(--navy) 0%, #2a6fc4 20%, var(--sky) 45%, #3b7fcf 62%, #262c78 78%, var(--navy-deep) 90%, var(--navy-deep) 100%);
  }
  .thank-you {
    position: absolute; left: 0; width: 574px; top: 308px; text-align: center;
    font-family: "Great Vibes", cursive; font-weight: 400; font-size: 82px; line-height: 1; color: var(--white);
  }
  .valued-client {
    position: absolute; left: 0; width: 574px; top: 422px; text-align: center;
    font-family: "Cinzel", serif; font-weight: 700; font-size: 33px; color: var(--white);
    letter-spacing: 0.5px;
  }
  .holiday-wish {
    position: absolute; left: 0; width: 574px; top: 704px; text-align: center;
    font-family: "Cinzel", serif; font-weight: 400; font-size: 26px; line-height: 36px;
    color: var(--text-soft); letter-spacing: 1px;
  }

  .address-side { position: absolute; left: 574px; top: 0; width: 626px; height: 856px; }
  .firm-block { position: absolute; left: 3px; width: 290px; top: 110px; text-align: center; }
  .firm-name {
    font-family: "Montserrat", sans-serif; font-weight: 500; font-size: 29px; line-height: 35px;
    letter-spacing: 1px; color: var(--grey-brand); margin-bottom: 12px;
  }
  .firm-contact {
    font-family: "Roboto Slab", serif; font-weight: 300; font-size: 20px; line-height: 27px;
    color: var(--ink-blue); font-style: normal;
  }
  .firm-contact .phone { margin-top: 5px; }
  .firm-contact .web { margin-top: 5px; color: var(--link-blue); letter-spacing: 0.5px; }
  .stamp-box {
    position: absolute; left: 384px; top: 64px; width: 152px; height: 166px;
    border: 2px solid var(--stamp-line);
  }
</style>
</head>
<body>
<main class="postcard">
  <section class="greeting-panel">
    <div class="celebration-art" role="img" aria-label="Red, white and blue balloons with confetti above a silhouetted crowd celebrating under blue lights"></div>
    <h1 class="thank-you">Thank You</h1>
    <p class="valued-client">For Being A Valued Client!</p>
    <p class="holiday-wish">Stay Safe And<br>Enjoy Your Independence Day<br>Celebrations!</p>
  </section>
  <section class="address-side">
    <div class="firm-block">
      <div class="firm-name">HADLEY LAW</div>
      <address class="firm-contact">
        <div>1420 W Maplecrest Ave</div>
        <div>Riverton, MO 65810</div>
        <div class="phone">Ph: (417) 555-0142</div>
        <div class="web">www.hadleylaw.com</div>
      </address>
    </div>
    <div class="stamp-box"></div>
  </section>
</main>
</body>
</html>
```